Need 3 posters for in-store display

Hi Marla,

Hope you are well.
I need 3 posters for display in my restaurant.

Poster 1: To be print in A1 size vertical
Title: BOWL-ERIFIC DEAL $19.50
Choose any Pho OR Noodle Salads
Choose Spring Rolls (5 rolls) OR Ricepaper Rolls (2 rolls)
Choose any Cans OR Water

What I like to see:
- These poster will be place near my counter so I want it to grab customer attention.
- You must use photos to show products
- Make it easy to understand and for customer to follow

Poster 2: To be print in A4 size vertical
Title: ADD TO YOUR ORDER
SpringRolls (Crab / vegetarian) $6 / 5 rolls
Extra Meat $2
Extra Noodles $1
Extra Vegs $1.5
Extra Tofu $2
Extra Crackling $3

Poster 3: To be print in A1 size vertical
Title: BROTH BONANZA FEAST
Catering Menu Options:
- PHO (Beef, Chicken, Vegan) $12.50 per bowl
- NOODLE SALADS (Beef, Chicken, BBQ Pork, Vegan) $12.50 per bowl
- SpringRolls (Crab / vegetarian) $12.50 for 10 rolls
- Ricepaper Rolls (Prawn, Beef, Chicken, BBQ Pork, Tofu) $12.5 / 5 rolls
- Fried Rice (Prawn, Tofu) $50 per tray (serve 5-6)

Terms & Conditions for All Catering Orders:
1) Minimum orders $200 (Pick-Up from shop Only)
2) All orders must be paid upfront
3) Requires $300 bond for Soup Tank
4) Please give us 48hours notice

• For the BOWL-ERIFIC DEAL
• it would be nice to have an image of the battle of water to visually complete the meal deal
• please see attachment of the Cedar Ridge Water

```html
<!DOCTYPE html>
<html lang="en">
<head>
<meta charset="utf-8">
<title>Add to Your Order</title>
<link href="https://fonts.googleapis.com/css2?family=Bebas+Neue&family=Kaushan+Script&family=Montserrat:wght@800&family=Arimo&family=Oswald:wght@400&display=swap" rel="stylesheet">
<style>
  :root {
    --night: #151515;
    --panel-orange: #f6962a;
    --panel-slate: #3e3e40;
    --ink: #3a3a3a;
    --accent: #f7941d;
    --white: #ffffff;
    --rice: #d9cbb0;
    --broth: #c9a77a;
    --board: #b08552;
    --basil: #3f6b2a;
  }
  html, body { margin: 0; padding: 0; overflow: hidden; background: var(--night); }
  .poster {
    position: relative;
    width: 849px;
    height: 1200px;
    overflow: hidden;
    background: var(--night);
  }
  .photo { position: absolute; }
  .photo--rice {
    left: 0; top: 480px; width: 190px; height: 300px;
    background: radial-gradient(ellipse at 30% 40%, var(--rice), #8c7a5e 70%, var(--night));
  }
  .photo--rolls {
    left: 0; top: 780px; width: 360px; height: 420px;
    background: linear-gradient(160deg, #c79a5f, var(--board) 55%, #6e5030);
  }
  .photo--pho {
    right: 0; top: 450px; width: 170px; height: 600px;
    background: linear-gradient(180deg, #e9e9e9 0%, #d8d3cb 40%, var(--broth) 70%, #eeeeee 100%);
  }
  .photo--basil {
    left: 360px; top: 960px; width: 489px; height: 240px;
    background: radial-gradient(ellipse at 70% 70%, var(--basil), #22361a 60%, var(--night) 100%);
  }
  .menu-card {
    position: absolute;
    left: 154px; top: 154px;
    width: 540px; height: 890px;
    border-radius: 26px;
    overflow: hidden;
    background: var(--panel-slate);
  }
  .menu-card__header {
    position: absolute; left: 0; top: 0;
    width: 100%; height: 358px;
    background: var(--panel-orange);
  }
  .title { position: absolute; color: var(--ink); margin: 0; line-height: 1; white-space: nowrap; }
  .title--add {
    left: 170px; top: 30px;
    font-family: "Bebas Neue", sans-serif;
    font-size: 180px;
    letter-spacing: 2px;
  }
  .title--your {
    left: 162px; top: 140px;
    font-family: "Kaushan Script", cursive;
    font-size: 80px;
  }
  .title--to { font-size: 42px; margin-right: 2px; }
  .title--order {
    left: 170px; top: 206px;
    font-family: "Oswald", sans-serif;
    font-weight: 400;
    font-size: 112px;
    transform: scaleX(0.78);
    transform-origin: left top;
  }
  .feature { position: absolute; color: var(--white); margin: 0; line-height: 1; white-space: nowrap; }
  .feature__name {
    left: 100px; top: 366px;
    font-family: "Kaushan Script", cursive;
    font-size: 58px;
  }
  .feature__desc {
    left: 30px; top: 450px;
    font-family: "Arimo", sans-serif;
    font-size: 40px;
  }
  .feature__price {
    left: 406px; top: 376px;
    font-family: "Bebas Neue", sans-serif;
    font-size: 78px;
    color: var(--accent);
  }
  .feature__qty {
    left: 406px; top: 452px;
    font-family: "Arimo", sans-serif;
    font-style: italic;
    font-size: 37px;
  }
  .extras {
    position: absolute; left: 0; top: 513px;
    width: 100%; margin: 0; padding: 0; list-style: none;
  }
  .extra {
    display: flex; align-items: center;
    height: 57px;
  }
  .extra__label {
    width: 346px;
    text-align: right;
    color: var(--white);
    white-space: nowrap;
  }
  .extra__kind {
    font-family: "Montserrat", sans-serif;
    font-weight: 800;
    font-size: 25px;
    letter-spacing: 1px;
  }
  .extra__item {
    font-family: "Kaushan Script", cursive;
    font-size: 37px;
    margin-left: 6px;
  }
  .extra__price {
    margin-left: 28px;
    font-family: "Bebas Neue", sans-serif;
    font-size: 56px;
    color: var(--accent);
    line-height: 1;
  }
  .brand {
    position: absolute;
    left: 274px; top: 1070px;
    width: 300px;
    margin: 0;
    display: flex; align-items: center; justify-content: center; gap: 10px;
    font-family: "Montserrat", sans-serif;
    font-weight: 800;
    font-size: 22px;
    letter-spacing: 1px;
    color: var(--white);
    white-space: nowrap;
  }
  .brand__dot {
    width: 14px; height: 14px;
    border-radius: 50%;
    background: var(--white);
  }
</style>
</head>
<body>
  <main class="poster">
    <div class="photo photo--rice" role="img" aria-label="Bowl of prawn fried rice with vegetables"></div>
    <div class="photo photo--rolls" role="img" aria-label="Crispy spring rolls on a wooden board with chilli dipping sauce"></div>
    <div class="photo photo--pho" role="img" aria-label="White bowls of pho with beef, herbs and onion"></div>
    <div class="photo photo--basil" role="img" aria-label="Fresh Thai basil leaves"></div>

    <section class="menu-card">
      <header class="menu-card__header">
        <h1 class="title title--add">ADD</h1>
        <p class="title title--your"><span class="title--to">to</span>your</p>
        <p class="title title--order">ORDER</p>
      </header>

      <p class="feature feature__name">Springrolls</p>
      <p class="feature feature__desc">(Crab/Vegetarian)</p>
      <p class="feature feature__price">$6</p>
      <p class="feature feature__qty">5 rolls</p>

      <ul class="extras">
        <li class="extra"><span class="extra__label"><span class="extra__kind">EXTRA</span><span class="extra__item">Meat</span></span><span class="extra__price">$2</span></li>
        <li class="extra"><span class="extra__label"><span class="extra__kind">EXTRA</span><span class="extra__item">Noodles</span></span><span class="extra__price">$1</span></li>
        <li class="extra"><span class="extra__label"><span class="extra__kind">EXTRA</span><span class="extra__item">Vegs</span></span><span class="extra__price">$1.5</span></li>
        <li class="extra"><span class="extra__label"><span class="extra__kind">EXTRA</span><span class="extra__item">Tofu</span></span><span class="extra__price">$2</span></li>
        <li class="extra"><span class="extra__label"><span class="extra__kind">EXTRA</span><span class="extra__item">Crackling</span></span><span class="extra__price">$3</span></li>
      </ul>
    </section>

    <p class="brand"><span class="brand__dot"></span>Saigon Lane</p>
  </main>
</body>
</html>
```